Business Card Design

We would like a business card that utilizes our current logo and keeps with the same feel - elegant and organic. Our farm isn't about mass production, it's about excellence, education, beautiful events and flowers - people, culture, and community.

Target Market(s)

Patrons to our farm who are interested in weddings, events, or our flowers and vegetables.

Contact Information for Business Card

Name, address, cell email (Danielle Hoskins, 2716 Wrenfield Rd, Longmont, CO 80503, cell 30.412.6638, email danielle@wrenfieldacres.com)

```html
<!DOCTYPE html>
<html lang="en">
<head>
<meta charset="utf-8">
<title>Wrenfield Acres – Business Card</title>
<link rel="stylesheet" href="https://fonts.googleapis.com/css2?family=Roboto:wght@400;500&display=swap">
<style>
  :root {
    --backdrop: #2b2b2b;
    --card-white: #ffffff;
    --sage: #76897a;
    --tan: #a98459;
    --ink: #333333;
    --shadow: rgba(0, 0, 0, 0.55);
  }
  * { margin: 0; padding: 0; box-sizing: border-box; }
  html, body {
    width: 1200px;
    height: 1200px;
    overflow: hidden;
    background: var(--backdrop);
    font-family: "Roboto", Arial, sans-serif;
  }
  .canvas {
    position: relative;
    width: 1200px;
    height: 1200px;
  }
  .card {
    position: absolute;
    left: 235px;
    width: 730px;
    height: 416px;
    box-shadow: 4px 6px 10px var(--shadow);
  }
  .card--front { top: 160px; background: var(--card-white); }
  .card--back  { top: 625px; background: var(--sage); }

  .brand-name {
    position: absolute;
    font-weight: 400;
    white-space: nowrap;
  }
  .card--front .brand-name {
    right: 62px;
    top: 70px;
    font-size: 34px;
    color: var(--sage);
    letter-spacing: 1px;
  }
  .card--back .brand-name {
    left: 0;
    right: 0;
    top: 158px;
    text-align: center;
    font-size: 56px;
    color: var(--card-white);
    letter-spacing: 2px;
  }

  .contact {
    position: absolute;
    left: 53px;
    top: 202px;
    color: var(--ink);
  }
  .contact__name {
    font-size: 25px;
    font-weight: 500;
    color: var(--sage);
    line-height: 1;
  }
  .contact__title {
    font-size: 18px;
    margin-top: 4px;
    line-height: 1.2;
  }
  .contact__address {
    font-size: 18px;
    line-height: 23px;
    margin-top: 21px;
  }
  .contact__lines {
    list-style: none;
    margin-top: 10px;
    font-size: 18px;
  }
  .contact__lines li {
    display: flex;
    align-items: center;
    height: 25px;
  }
  .contact__icon {
    width: 14px;
    height: 14px;
    margin-right: 10px;
    fill: var(--tan);
  }

  .website {
    position: absolute;
    left: 0;
    right: 0;
    top: 352px;
    text-align: center;
    color: var(--card-white);
    font-size: 19px;
    letter-spacing: 1px;
  }
</style>
</head>
<body>
<main class="canvas">
  <section class="card card--front" aria-label="Card front">
    <p class="brand-name">Wrenfield Acres</p>
    <div class="contact">
      <h1 class="contact__name">DANIELLE HOSKINS</h1>
      <p class="contact__title">Founder and CEO</p>
      <p class="contact__address">2716 Wrenfield Rd, Longmont<br>CO 80503</p>
      <ul class="contact__lines">
        <li>
          <svg class="contact__icon" viewBox="0 0 24 24" aria-hidden="true">
            <path d="M6.6 10.8a15.1 15.1 0 0 0 6.6 6.6l2.2-2.2a1 1 0 0 1 1-.25 11.4 11.4 0 0 0 3.6.57 1 1 0 0 1 1 1V20a1 1 0 0 1-1 1A17 17 0 0 1 3 4a1 1 0 0 1 1-1h3.5a1 1 0 0 1 1 1c0 1.25.2 2.45.57 3.57a1 1 0 0 1-.25 1z"/>
          </svg>
          030.412.6638
        </li>
        <li>
          <svg class="contact__icon" viewBox="0 0 24 24" aria-hidden="true">
            <path d="M2 5h20v2l-10 6L2 7z"/>
            <path d="M2 9l10 6 10-6v10H2z"/>
          </svg>
          danielle@wrenfieldacres.com
        </li>
      </ul>
    </div>
  </section>

  <section class="card card--back" aria-label="Card back">
    <p class="brand-name">Wrenfield Acres</p>
    <p class="website">www.wrenfieldacres.com</p>
  </section>
</main>
</body>
</html>
```